Business Card Design

Im a small business that specialises in all aspects of sign installation, big and small, domestic and commercial. I have a construction and carpentry background. I'm after a professional looking business card, that has my logo as the forefront of the card incorporating the same colours as the my logo. No slogan as yet, but open to suggestions. The final design should communicate quality and class workmanship.

Target Market(s)

Managers and Owners of businesses

Industry/Entity Type

Small Business

Contact Information for Business Card

Dorian Feltwick
Mob: 0491275830
Email: dkf.fitouts@quillmail.example

Sign Installation
Property Improvement and Maintenance
Trade Services

Colors
dbdbdb
000000
ffffff

Requirements
Must have
• Logo
My name
My contact details
What I specialise in
Nice to have
• background image/images that are only just noticeable and do not take away from the logo or text.
Should not have
• No colours that contrast from my logo
No heavy machinery images to be used
Logo must stand out

```html
<!DOCTYPE html>
<html lang="en">
<head>
<meta charset="utf-8">
<title>DKF Installations – Business Card</title>
<link href="https://fonts.googleapis.com/css2?family=Bebas+Neue&display=swap" rel="stylesheet">
<style>
  :root {
    --card-dark: #0c0d0e;
    --card-mid: #34393c;
    --panel-white: #ffffff;
    --brand-ink: #000000;
    --text-light: #dbdbdb;
    --text-shadow: rgba(0, 0, 0, 0.85);
  }
  * { margin: 0; padding: 0; box-sizing: border-box; }
  html, body {
    width: 1200px;
    height: 741px;
    overflow: hidden;
    background: var(--card-dark);
  }
  .card {
    position: relative;
    width: 1200px;
    height: 741px;
    background: radial-gradient(ellipse 48% 55% at 50% 55%, var(--card-mid) 0%, #1d2022 55%, var(--card-dark) 100%);
    font-family: "Bebas Neue", "Arial Narrow", sans-serif;
    color: var(--text-light);
    text-align: center;
  }
  .logo-panel {
    position: absolute;
    left: 357px;
    top: 121px;
    width: 486px;
    height: 200px;
    background: var(--panel-white);
    display: flex;
    align-items: center;
    justify-content: center;
  }
  .logo-name {
    font-family: "Bebas Neue", "Arial Narrow", sans-serif;
    font-size: 56px;
    line-height: 1;
    letter-spacing: 3px;
    color: var(--brand-ink);
    white-space: nowrap;
  }
  .contact-line {
    position: absolute;
    left: 0;
    width: 100%;
    text-shadow: 3px 4px 5px var(--text-shadow);
    white-space: nowrap;
  }
  .owner-name {
    top: 359px;
    font-size: 53px;
    letter-spacing: 11px;
  }
  .mobile {
    top: 456px;
    font-size: 40px;
    letter-spacing: 7px;
  }
  .email {
    top: 491px;
    font-size: 30px;
    letter-spacing: 3.5px;
  }
  .services {
    top: 547px;
    font-size: 24px;
    letter-spacing: 3.6px;
  }
</style>
</head>
<body>
  <div class="card">
    <div class="logo-panel">
      <div class="logo-name">DKF Installations</div>
    </div>

    <div class="contact-line owner-name">Dorian Feltwick</div>
    <div class="contact-line mobile">Mob: 0491275830</div>
    <div class="contact-line email">Email: dkf.fitouts@quillmail.example</div>
    <div class="contact-line services">Sign Installation Property Improvement and Maintenance Trade Services</div>
  </div>
</body>
</html>
```